Courier Business needs a Business Card Design !!!

My new company needs a business card design. Our company name is Swift Heron Courier & Delivery Services. We will be servicing residential , government and business clients in the City of Yellowknife, Northwest Territories, Canada. I would like the following information included on the card: Name- Walter Pruitt. Title- Owner. Company- Swift Heron Courier & Delivery Services. Address- PO Box 5918 , Yellowknife , NWT, X1A 4K3. Phone- 867-392-7184. Email- swiftheroncourieryk@mailbox-example.net. Facebook- www.socialpage-example.net/swiftheroncourieryk. I would like my double sided card to be the standard size of 84mm x 55mm. No borders. Use CMYK mode.1039x 697 pixels at least. I would like my logo to take up at least one quarter of the area of one side of the card. Text should be at least 8 point with perhaps my name being 10 point and my company name being 12-15 point . It should have clear readable font. Please use one or two bold colors. I am trying to attract the business community so a professional look might be best. My tag line is " On Time Every Time ". Nice safe margins please. We will be providing fast, reliable and professional delivery of envelopes and small packages within the City of Yellowknife. We offer 100% satisfaction or a complete refund. I have included a file of our logo. I like black, blue and red but am willing to look at what you feel would work best. I do not really like white as a background color.

Target Market(s)

Professionals , business owners. 30-50 years old

Industry/Entity Type

Residential

Contact Information for Business Card

As noted in brief

Font styles to use
Serif
Sans Serif

Colors
000000
0255a3
f04a50

Requirements
Must have
• My contact info. My logo
Nice to have
• Simple elegant design but still catches the eye
Should not have
• White background color

```html
<!DOCTYPE html>
<html lang="en">
<head>
<meta charset="utf-8">
<title>Swift Heron Courier &amp; Delivery Services – Business Card</title>
<link rel="stylesheet" href="https://fonts.googleapis.com/css2?family=Lato:wght@300;400;900&display=swap">
<style>
  :root {
    --backdrop: #d9d9d9;
    --card: #000000;
    --blue: #0255a3;
    --blue-bright: #1a73c9;
    --coral: #f04a50;
    --text: #f2f2f2;
  }
  * { box-sizing: border-box; margin: 0; padding: 0; }
  html, body {
    width: 1200px; height: 745px; overflow: hidden;
    background: var(--backdrop);
    font-family: "Lato", sans-serif;
  }
  .sheet { position: relative; width: 1200px; height: 745px; }
  .card {
    position: absolute;
    width: 540px; height: 354px;
    background: var(--card);
    overflow: hidden;
  }
  .card--front { left: 40px; top: 60px; }
  .card--back { left: 620px; top: 331px; }

  .brand {
    display: flex; align-items: center; gap: 10px;
    color: var(--coral);
    font-weight: 900;
    text-transform: uppercase;
    line-height: 1.05;
  }
  .brand__dot {
    flex: none;
    width: 14px; height: 14px; border-radius: 50%;
    background: var(--blue-bright);
  }
  .card--front .brand {
    position: absolute; left: 50%; top: 50%;
    transform: translate(-50%, -50%);
    font-size: 24px; width: 330px;
  }
  .card--back .brand {
    position: absolute; left: 372px; top: 40px;
    width: 150px; font-size: 15px;
  }

  .divider {
    position: absolute; left: 356px; top: 110px;
    width: 3px; height: 244px;
    background: var(--blue);
  }

  .holder { position: absolute; left: 60px; top: 122px; }
  .holder__name {
    color: var(--text); font-weight: 300; font-size: 24px; letter-spacing: 0.5px;
  }
  .holder__title {
    color: var(--blue-bright); font-weight: 400; font-size: 15px;
    margin-left: 82px; margin-top: -2px;
  }

  .contacts {
    position: absolute; left: 42px; top: 196px;
    list-style: none; width: 300px;
  }
  .contacts li {
    display: flex; align-items: flex-start; gap: 10px;
    color: var(--text); font-weight: 300; font-size: 12px; line-height: 1.3;
    margin-bottom: 12px;
  }
  .contacts svg { flex: none; width: 13px; height: 13px; fill: var(--blue-bright); margin-top: 1px; }
  .contacts .social-mark { flex: none; width: 12px; height: 12px; background: var(--blue-bright); margin-top: 2px; }
</style>
</head>
<body>
<main class="sheet">
  <section class="card card--front" aria-label="Card front">
    <div class="brand"><span class="brand__dot"></span><span>Swift Heron Courier &amp; Delivery Services</span></div>
  </section>

  <section class="card card--back" aria-label="Card back">
    <div class="brand"><span>Swift Heron Courier &amp; Delivery Services</span></div>
    <div class="divider"></div>

    <div class="holder">
      <p class="holder__name">Walter Pruitt</p>
      <p class="holder__title">Owner</p>
    </div>

    <ul class="contacts">
      <li>
        <svg viewBox="0 0 24 24" aria-hidden="true"><path d="M6.6 10.8a15.1 15.1 0 0 0 6.6 6.6l2.2-2.2a1 1 0 0 1 1-.25 11.4 11.4 0 0 0 3.6.57 1 1 0 0 1 1 1V20a1 1 0 0 1-1 1A17 17 0 0 1 3 4a1 1 0 0 1 1-1h3.5a1 1 0 0 1 1 1c0 1.25.2 2.45.57 3.57a1 1 0 0 1-.25 1z"/></svg>
        <span>867-392-7184</span>
      </li>
      <li>
        <svg viewBox="0 0 24 24" aria-hidden="true"><path d="M12 2a7 7 0 0 0-7 7c0 5.25 7 13 7 13s7-7.75 7-13a7 7 0 0 0-7-7zm0 9.5A2.5 2.5 0 1 1 12 6.5a2.5 2.5 0 0 1 0 5z"/></svg>
        <span>PO Box 5918 , Yellowknife ,<br>NWT, X1A 4K3</span>
      </li>
      <li>
        <svg viewBox="0 0 24 24" aria-hidden="true"><path d="M2 5h20v14H2z M2 5l10 8 10-8" /><path d="M2 5l10 8 10-8v2l-10 8L2 7z" fill="#000"/></svg>
        <span>swiftheroncourieryk@mailbox-example.net</span>
      </li>
      <li>
        <span class="social-mark"></span>
        <span style="font-size:11px">www.socialpage-example.net/swiftheroncourieryk</span>
      </li>
    </ul>
  </section>
</main>
</body>
</html>
```